Etiketten für Wein
Zielgruppe
Weinkellerei aus Baden (Deutschland) mit Fokus im Lebensmittelhandel in Deutschland
Zielgruppe: Discount-Kunden, Männlich/Weiblich, Alter: 25-60 Jahre, wird für unter € 4,-/Fl. verkauft.
Aufgabenstellung
Wir suchen ein Frontetikett für einen Riesling aus Rheinhessen. Das Etikett sollte zeitlos, schlicht, modern anmutend sein. Hochwertiges Etikettenpapier (zweiteilig).
Weinbeschreibung:
Aussehen: helles gelb,
Geruch: Frische Frucht, heimische und exotische Früchte,
Geschmack: Feines Spiel von Frucht und animierender Säure
Anforderungen Etikett:
Maße: Höhe max. 120mm/Breite max. 80mm (darf auch kleiner oder quadratisch sein)
SK Etikett, Naturstruktur bis 90g (m²) (gerne zweiteilig)
Eine figürliche Etikettenkontur ist möglich, es wird aber am rechten Etikettenrand eine gerade Spendekante benötigt um das Etikett maschinell verarbeiten zu können.
Als Flasche wird eine 0,75 L Schlegelflasche (Farbe: feuille morte) eingesetzt.
Verschluss: Longcap
Mögliche Veredelungen: Quelllack, Prägungen, Heissfolie, Glanzlack
Pflichtangaben:
- Rheinhessen
- Auerbacher Lindenhang Riesling Qualitätswein trocken (Rebsorte 'Riesling' gerne prominent darstellen)
- Jahrgang 2023
SK Etikett, Naturstruktur bis 90g (m²) (gerne zweiteilig - einteilig aber auch möglich)

```html
<!DOCTYPE html>
<html lang="de">
<head>
<meta charset="utf-8">
<title>Riesling Etikett – Rheinhessen</title>
<link href="https://fonts.googleapis.com/css2?family=Montserrat:wght@300;600;700;800&family=Cinzel:wght@500&display=swap" rel="stylesheet">
<style>
  :root{
    --label-yellow:#efdb33;
    --ink:#231815;
    --riesling-red:#e8420f;
    --ornament-tone:#6b5a22;
    --page:#ffffff;
  }
  *{margin:0;padding:0;box-sizing:border-box}
  html,body{width:1200px;height:2317px;overflow:hidden;background:var(--page)}
  body{position:relative;font-family:"Montserrat",sans-serif;color:var(--ink)}

  .front-label{position:absolute;left:200px;top:120px;width:800px;height:1200px;background:var(--label-yellow)}
  .band{position:absolute;left:0;width:100%;background:var(--ink)}
  .band--top{top:0;height:51px}
  .band--bottom{bottom:0;height:48px}
  .rule{position:absolute;left:0;width:100%;height:5px;background:var(--ink)}
  .rule--top{top:58px}
  .rule--bottom{bottom:56px}

  .region-name{position:absolute;left:0;width:100%;text-align:center;font-weight:700;text-transform:uppercase;color:var(--ink)}
  .front-label .region-name{top:165px;font-size:64px;line-height:80px;letter-spacing:6px}
  .neck-label .region-name{top:350px;font-size:34px;line-height:44px;letter-spacing:3px}

  .quality-block{position:absolute;left:0;width:100%;text-align:center;font-weight:700;text-transform:uppercase}
  .front-label .quality-block{top:285px;font-size:31px;line-height:36px}

  .divider{position:absolute;left:0;width:100%;height:64px}
  .divider .line{position:absolute;top:31px;height:2px;background:var(--ink)}
  .divider .line--left{left:103px;width:127px}
  .divider .line--right{right:103px;width:127px}
  .divider .ornament{position:absolute;left:240px;width:320px;top:12px;height:40px;border-radius:50%;
    background:radial-gradient(ellipse at center,var(--ink) 0%,var(--ornament-tone) 55%,rgba(107,90,34,0) 72%)}
  .divider--upper{top:436px}
  .divider--lower{top:968px}

  .site-name{position:absolute;top:545px;left:0;width:100%;display:flex;align-items:center;justify-content:center;gap:20px;
    font-weight:600;font-size:50px;letter-spacing:1px}
  .dash{display:block;height:3px;background:var(--ink)}
  .site-name .dash{width:50px}

  .variety{position:absolute;top:592px;left:0;width:100%;text-align:center;font-family:"Cinzel",serif;font-weight:500;
    font-size:164px;line-height:170px;color:var(--riesling-red);letter-spacing:-3px}

  .vintage-label{position:absolute;top:805px;left:0;width:100%;text-align:center;font-weight:300;font-size:30px;letter-spacing:26px;padding-left:26px}
  .vintage-year{position:absolute;top:845px;left:0;width:100%;text-align:center;font-weight:800;font-size:86px;line-height:100px}

  .volume{position:absolute;top:1064px;left:0;width:100%;display:flex;align-items:center;justify-content:center;gap:28px;font-weight:700;font-size:38px}
  .volume .dash{width:105px}

  .neck-label{position:absolute;left:250px;top:1480px;width:700px;height:531px;background:var(--label-yellow)}
  .neck-label .quality-block{top:440px;font-size:16px;line-height:19px}
  .neck-divider{position:absolute;top:410px;left:280px;width:140px;height:18px;display:flex;align-items:center}
  .neck-divider .ornament{width:100%;height:14px;border-radius:50%;
    background:radial-gradient(ellipse at center,var(--ink) 0%,var(--ornament-tone) 50%,rgba(107,90,34,0) 72%)}
</style>
</head>
<body>

<section class="front-label" aria-label="Frontetikett Riesling">
  <div class="band band--top"></div>
  <div class="rule rule--top"></div>

  <p class="region-name">Rheinhessen</p>

  <div class="quality-block">
    <p>Qualitätswein</p>
    <p>Trocken</p>
    <p>Auerbacher</p>
  </div>

  <div class="divider divider--upper">
    <span class="line line--left"></span>
    <span class="ornament" role="img" aria-label="Florales Zierornament"></span>
    <span class="line line--right"></span>
  </div>

  <div class="site-name"><span class="dash"></span>LINDENHANG<span class="dash"></span></div>
  <h1 class="variety">RIESLING</h1>

  <p class="vintage-label">JAHRGANG</p>
  <p class="vintage-year">2023</p>

  <div class="divider divider--lower">
    <span class="line line--left"></span>
    <span class="ornament" role="img" aria-label="Florales Zierornament"></span>
    <span class="line line--right"></span>
  </div>

  <div class="volume"><span class="dash"></span>0,75 L<span class="dash"></span></div>

  <div class="rule rule--bottom"></div>
  <div class="band band--bottom"></div>
</section>

<section class="neck-label" aria-label="Kapsel- und Halsetikett">
  <p class="region-name">Rheinhessen</p>
  <div class="neck-divider"><span class="ornament" role="img" aria-label="Kleines florales Zierornament"></span></div>
  <div class="quality-block">
    <p>Qualitätswein</p>
    <p>Trocken</p>
    <p>Auerbacher</p>
  </div>
</section>

</body>
</html>
```